Business Card needed for Drainor, a growing Septic Service company

Drainor, a growing local septic service company in Pennsylvania, needs updated business cards. We'd like the business card to feature our logo and communicate that we provide Septic Pumping, Installations/Repairs, Restroom Rentals, and 24/7 Emergency Service. The business card should be eye-catching, bold, and clean/simple. We have been in business almost 10 years and would like to expand and update our business brand and image.

Target Market(s)

Residential and Commercial, New and Current Homeowners

Industry/Entity Type

Service

Contact Information for Business Card

Contact on the business card should be: Dean Harlow Owner & Operator
Phone: 610-555-0187
Email: service@drainor-example.com
Website: www.drainor-example.com
Address: 812 Millbrook Lane Easton PA 18042

Font styles to use
Sans Serif

Colors

Designer to choose colors to be used in the design.

Requirements
Must have
• Feature logo on both side of business card.
Nice to have
• We envision the contact information on one side and our services listed on the other side. Utilize the green from the symbol in our logo as part of the design, overall design color scheme should be white, grey, black.

```html
<!DOCTYPE html>
<html lang="en">
<head>
<meta charset="utf-8">
<title>Drainor – Business Card</title>
<link href="https://fonts.googleapis.com/css2?family=Montserrat:wght@400;500;600;700&family=Figtree:wght@400;500&display=swap" rel="stylesheet">
<style>
  :root {
    --ink: #1b2312;
    --panel: #1c2413;
    --green: #82e31c;
    --white: #ffffff;
    --text-dark: #1d2216;
  }
  * { margin: 0; padding: 0; box-sizing: border-box; }
  html, body {
    width: 1200px; height: 686px; overflow: hidden; background: var(--white);
  }
  .card {
    position: relative; width: 1200px; height: 686px; overflow: hidden;
    background: var(--white);
    font-family: "Montserrat", sans-serif;
  }
  .panel-wrap {
    position: absolute; inset: 0;
    filter: drop-shadow(-6px 0 6px rgba(0,0,0,0.35));
  }
  .panel {
    position: absolute; inset: 0; background: var(--panel);
    clip-path: polygon(683px 0, 1200px 0, 1200px 686px, 543px 686px);
  }

  /* Brand */
  .brand {
    position: absolute; left: 65px; top: 202px; height: 68px;
    display: flex; align-items: center; gap: 18px;
  }
  .brand-mark { width: 68px; height: 68px; background: var(--green); }
  .brand-name {
    font-family: "Montserrat", sans-serif; font-weight: 700;
    font-size: 62px; letter-spacing: 2px; color: var(--ink); line-height: 1;
  }

  /* Services */
  .services-title {
    position: absolute; left: 65px; top: 293px; width: 383px; height: 38px;
    background: var(--ink); color: var(--white);
    font-weight: 600; font-size: 24px; line-height: 38px; text-align: center;
    letter-spacing: 0.5px;
  }
  .services-list {
    position: absolute; left: 65px; top: 342px; list-style: none;
    color: var(--text-dark); font-size: 28px; font-weight: 500;
  }
  .services-list li { height: 38px; line-height: 38px; }

  /* Contact side */
  .person {
    position: absolute; right: 74px; top: 148px; width: 380px; text-align: right;
  }
  .person-name {
    color: var(--white); font-weight: 600; font-size: 46px; line-height: 48px;
    letter-spacing: 0.5px; white-space: nowrap;
  }
  .person-rule {
    position: absolute; left: 746px; top: 205px; width: 380px; height: 2px;
    background: var(--white);
  }
  .person-role {
    position: absolute; right: 74px; top: 222px;
    color: var(--green); font-size: 25px; font-weight: 400; letter-spacing: 0.3px;
  }
  .contact {
    position: absolute; right: 74px; display: flex; align-items: center; gap: 22px;
    font-family: "Figtree", sans-serif; color: var(--white); font-size: 27px;
  }
  .contact-text { text-align: right; line-height: 32px; white-space: nowrap; }
  .contact-icon { width: 54px; height: 54px; flex: none; }
  .contact--phone { top: 291px; }
  .contact--email { top: 357px; }
  .contact--web { top: 422px; }
  .contact--address { top: 486px; }
</style>
</head>
<body>
<div class="card">
  <div class="panel-wrap"><div class="panel"></div></div>

  <div class="brand">
    <div class="brand-mark"></div>
    <div class="brand-name">DRAINOR</div>
  </div>

  <div class="services-title">SERVICES WE PROVIDE:</div>
  <ul class="services-list">
    <li>- SEPTIC PUMPING</li>
    <li>- INSTALLATIONS/REPAIRS</li>
    <li>- RESTROOM RENTALS</li>
    <li>- 24/7 EMERGENCY SERVICE</li>
  </ul>

  <div class="person"><div class="person-name">DEAN HARLOW</div></div>
  <div class="person-rule"></div>
  <div class="person-role">OWNER AND OPERATOR</div>

  <div class="contact contact--phone">
    <span class="contact-text">610-555-0187</span>
    <svg class="contact-icon" viewBox="0 0 54 54" aria-hidden="true">
      <circle cx="27" cy="27" r="27" fill="#82e31c"/>
      <path d="M19 15c1.5-1 3-.6 3.8.8l2.4 4.2c.7 1.3.3 2.6-.9 3.4l-1.5 1c1.2 2.8 3.4 5 6.2 6.2l1-1.5c.8-1.2 2.1-1.6 3.4-.9l4.2 2.4c1.4.8 1.8 2.3.8 3.8l-1.4 2c-1.2 1.6-3.3 2.2-5.2 1.5C23.8 35.8 18.2 30.2 16 22.8c-.7-1.9-.1-4 1.5-5.2z" fill="#1c2413"/>
    </svg>
  </div>

  <div class="contact contact--email">
    <span class="contact-text">service@drainor-example.com</span>
    <svg class="contact-icon" viewBox="0 0 54 54" aria-hidden="true">
      <circle cx="27" cy="27" r="27" fill="#82e31c"/>
      <rect x="15" y="18" width="24" height="18" rx="1.5" fill="none" stroke="#1c2413" stroke-width="2.6"/>
      <path d="M15.5 19l11.5 9 11.5-9" fill="none" stroke="#1c2413" stroke-width="2.6"/>
    </svg>
  </div>

  <div class="contact contact--web">
    <span class="contact-text">www.drainor-example.com</span>
    <svg class="contact-icon" viewBox="0 0 54 54" aria-hidden="true">
      <circle cx="27" cy="27" r="23" fill="#82e31c"/>
      <g fill="none" stroke="#1c2413" stroke-width="2.2">
        <line x1="4" y1="27" x2="50" y2="27"/>
        <line x1="27" y1="4" x2="27" y2="50"/>
        <ellipse cx="27" cy="27" rx="11" ry="23"/>
        <path d="M8 16h38M8 38h38"/>
      </g>
    </svg>
  </div>

  <div class="contact contact--address">
    <span class="contact-text">812 Millbrook Lane Easton<br>PA 18042</span>
    <svg class="contact-icon" viewBox="0 0 54 54" aria-hidden="true">
      <ellipse cx="27" cy="45" rx="20" ry="6" fill="#82e31c"/>
      <ellipse cx="27" cy="45" rx="10" ry="2.6" fill="#1c2413"/>
      <path d="M27 45C20 36 14 28 14 19a13 13 0 0 1 26 0c0 9-6 17-13 26z" fill="#82e31c" stroke="#1c2413" stroke-width="1.5"/>
      <circle cx="27" cy="19" r="5" fill="#1c2413"/>
    </svg>
  </div>
</div>
</body>
</html>
```